Modern corporate energy/fuel business need business card design

Business card required for company founder. Korvan Integrated Energy is a Australian based modern energy/fuel provider. We offer specialised solutions to businesses using fossil fuels through renewable energy solutions.

I would like one side with specific information (name, address etc)

The other side to be bold, professional company name & logo. Striking.

Target Market(s)

B2B. Transport, mining, councils, environmentalist,

Industry/Entity Type

Petroleum

Contact Information for Business Card

Name; Oliver Brentham
Position; Director
Email; obrentham@korvanspec.com.au
Address; PO Box 487, Kellmorrow, NSW, 2999
Website; www.korvanspec.com.au

Colors

Designer to choose colors to be used in the design.

Requirements
Must have
• Clean, easy to read, professional & strong theme
Should not have
• too many colours, busy layout,

```html
<!DOCTYPE html>
<html lang="en">
<head>
<meta charset="utf-8">
<title>Korvan Integrated Energy – Business Card</title>
<link href="https://fonts.googleapis.com/css2?family=Roboto:ital,wght@0,400;0,500;1,400&display=swap" rel="stylesheet">
<style>
  :root {
    --stage: #3b3c40;
    --card: #141414;
    --card-edge: #1d1d1e;
    --brand-blue: #1f5a8a;
    --brand-orange: #f57a14;
    --text-grey: #8a8d91;
    --text-white: #f1f1f1;
  }
  * { box-sizing: border-box; margin: 0; padding: 0; }
  html, body { width: 1200px; height: 1200px; overflow: hidden; }
  body {
    background: var(--stage);
    font-family: "Roboto", Arial, sans-serif;
    position: relative;
  }
  .card {
    position: absolute;
    left: 150px;
    width: 900px;
    height: 514px;
    border-radius: 34px;
    background: linear-gradient(160deg, var(--card-edge) 0%, var(--card) 60%, #0d0d0d 100%);
    box-shadow: 0 18px 40px rgba(0,0,0,0.45);
    overflow: hidden;
  }
  .card--front { top: 50px; }
  .card--back { top: 620px; }

  .world-map {
    position: absolute;
    left: 90px; top: 40px;
    width: 720px; height: 380px;
    border-radius: 40px;
    background: radial-gradient(ellipse at center, #1c1c1d 0%, rgba(20,20,20,0) 70%);
  }

  .brand {
    position: absolute;
    display: flex;
    align-items: center;
    gap: 22px;
  }
  .brand__dot {
    width: 110px; height: 110px;
    border-radius: 50%;
    background: var(--brand-orange);
    flex: none;
  }
  .brand__name {
    color: var(--brand-blue);
    font-weight: 500;
    line-height: 1;
    text-transform: uppercase;
  }
  .brand__name .word { display: block; font-size: 72px; letter-spacing: 8px; }
  .brand__name .tag { display: block; font-size: 17px; letter-spacing: 9px; margin-top: 12px; }

  .card--front .brand { left: 0; right: 0; top: 160px; justify-content: center; }

  .front__url {
    position: absolute;
    left: 0; right: 0; bottom: 62px;
    text-align: center;
    color: var(--text-white);
    font-size: 20px;
    letter-spacing: 0.5px;
  }
  .front__url .accent { color: var(--brand-orange); font-weight: 500; }

  .card--back .brand { left: 400px; top: 60px; }
  .card--back .brand__dot { width: 90px; height: 90px; }
  .card--back .brand__name .word { font-size: 58px; letter-spacing: 7px; }
  .card--back .brand__name .tag { font-size: 15px; letter-spacing: 8px; }

  .holder { position: absolute; left: 70px; top: 215px; }
  .holder__name {
    color: var(--brand-blue);
    font-size: 26px;
    font-weight: 500;
    text-transform: uppercase;
  }
  .holder__role {
    color: var(--text-grey);
    font-size: 18px;
    font-style: italic;
    margin-top: 2px;
  }
  .divider {
    position: absolute;
    left: 70px; right: 110px; top: 300px;
    height: 2px;
    background: var(--brand-orange);
  }
  .address {
    position: absolute;
    left: 70px; top: 322px;
    color: var(--text-grey);
    font-size: 18px;
    line-height: 1.45;
  }
  .contacts {
    position: absolute;
    right: 110px; top: 378px;
    list-style: none;
    color: var(--text-grey);
    font-size: 19px;
  }
  .contacts li { display: flex; align-items: center; gap: 10px; margin-bottom: 8px; }
  .contacts svg { width: 18px; height: 18px; flex: none; }
</style>
</head>
<body>

<section class="card card--front" aria-label="Card front">
  <div class="world-map" role="img" aria-label="Faint world map backdrop"></div>
  <div class="brand">
    <span class="brand__dot"></span>
    <span class="brand__name"><span class="word">Korvan</span><span class="tag">Integrated Energy</span></span>
  </div>
  <p class="front__url">www.<span class="accent">korvanspec</span>.com.au</p>
</section>

<section class="card card--back" aria-label="Card back">
  <div class="brand">
    <span class="brand__dot"></span>
    <span class="brand__name"><span class="word">Korvan</span><span class="tag">Integrated Energy</span></span>
  </div>
  <div class="holder">
    <h1 class="holder__name">Oliver Brentham</h1>
    <p class="holder__role">Director</p>
  </div>
  <div class="divider"></div>
  <p class="address">PO Box 487, Kellmorrow,<br>NSW, 2999</p>
  <ul class="contacts">
    <li>
      <svg viewBox="0 0 20 20" aria-hidden="true"><rect x="1.5" y="4" width="17" height="12" rx="1.5" fill="none" stroke="#f57a14" stroke-width="2"/><path d="M2 5l8 6 8-6" fill="none" stroke="#f57a14" stroke-width="2"/></svg>
      obrentham@korvanspec.com.au
    </li>
    <li>
      <svg viewBox="0 0 20 20" aria-hidden="true"><circle cx="10" cy="10" r="8" fill="none" stroke="#f57a14" stroke-width="1.8"/><ellipse cx="10" cy="10" rx="3.5" ry="8" fill="none" stroke="#f57a14" stroke-width="1.5"/><path d="M2 10h16" stroke="#f57a14" stroke-width="1.5"/></svg>
      www.korvanspec.com.au
    </li>
  </ul>
</section>

</body>
</html>
```